Stated Income Loans

Flyer design to be used on social media platforms (i.e. Chatterbox, Snapgrove etc.)

Target Market(s)

Real Estate Investors

Requirements
Must have
• INVESTOR STATED INCOME LOANS
• "IT'S TIME TO THINK BIG"
• * Purchase or Refinance up to 3 Million
• * No Income Docs or Bank Statements
• * Vacant Properties Allowed
• * Minimum Credit Score 620
• * Cash Out up to 80%
• Same Day Pre-Approval
• 20-30 Day Close
• Call Marcus Whitfield today...
• Bluecrest Lending Group, Inc.
• Phone (800) 641-2957 x 17
• Direct (240) 958-2074
• www.bluecrestlendhub.com
• NMLS #583617 / #47081
Should not have
• Do not use same color scheme as website. Be creative.

```html
<!DOCTYPE html>
<html lang="en">
<head>
<meta charset="utf-8">
<title>Investor Stated Income Loans</title>
<link href="https://fonts.googleapis.com/css2?family=Jost:wght@400;500;600;700&display=swap" rel="stylesheet">
<style>
:root{
  --green:#5b7a1f;
  --green-dark:#4a6418;
  --ink:#1c1c1c;
  --stage:#8c8c8c;
  --paper:#ffffff;
  --paper-tint:#f1f1f1;
}
*{margin:0;padding:0;box-sizing:border-box}
html,body{width:960px;height:1200px;overflow:hidden;background:var(--stage)}
body{font-family:"Jost",sans-serif;color:var(--ink)}
.flyer{position:absolute;left:72px;top:23px;width:816px;height:1154px;overflow:hidden;
  background:linear-gradient(160deg,var(--paper) 0%,var(--paper-tint) 45%,var(--paper) 100%)}
.header-band{position:absolute;left:0;top:0;width:816px;height:97px;background:var(--green);
  display:flex;align-items:center;justify-content:center}
.header-band h1{color:#fff;font-weight:700;font-size:39px;letter-spacing:1px}
.hero-photo{position:absolute;left:0;top:97px;width:816px;height:389px;
  background:linear-gradient(180deg,#2a2a2a 0%,#8f8f8f 30%,#5c5c5c 60%,#1e1e1e 100%)}
.hero-panel{position:absolute;left:0;top:237px;width:447px;height:196px;background:rgba(91,122,31,.85)}
.hero-line{position:absolute;left:48px;color:#fff;line-height:1;white-space:nowrap}
.hero-its{top:246px;font-size:54px;font-weight:400}
.hero-time{top:304px;font-size:62px;font-weight:400}
.hero-big{top:364px;font-size:66px;font-weight:700}
.feature{position:absolute;width:200px;text-align:center;font-size:16px;line-height:1.3;font-weight:500}
.feature svg{display:block;margin:0 auto 20px;stroke:var(--green);fill:none;stroke-width:3;stroke-linecap:round;stroke-linejoin:round}
.brand-card{position:absolute;left:28px;top:881px;width:292px;height:191px;background:#fff;
  box-shadow:0 4px 12px rgba(0,0,0,.25);display:flex;align-items:center;justify-content:center;gap:10px;padding:0 16px}
.brand-card .mark{width:22px;height:22px;border-radius:50%;background:var(--green);flex:none}
.brand-card .brand-name{color:var(--green);font-weight:600;font-size:19px;line-height:1.2}
.call-line{position:absolute;left:344px;top:904px;font-size:18px;font-weight:500;white-space:nowrap}
.call-line strong{color:var(--green);font-weight:600}
.contact-band{position:absolute;left:320px;top:940px;width:496px;height:116px;background:var(--green)}
.contact-list{position:absolute;left:344px;top:952px;list-style:none;color:#fff;font-size:16px;font-weight:500;line-height:23.5px}
.agent-photo{position:absolute;left:634px;top:862px;width:178px;height:194px;
  background:linear-gradient(180deg,#6a5546 0%,#3a2e28 45%,#1d1d22 100%)}
.social{position:absolute;top:1099px;left:354px;display:flex;gap:12px}
.social span{width:28px;height:28px;border-radius:50%;border:2px solid var(--green)}
.footer-rule{position:absolute;left:0;bottom:0;width:816px;height:7px;background:var(--green)}
</style>
</head>
<body>
<main class="flyer">
  <header class="header-band"><h1>INVESTOR STATED INCOME LOANS</h1></header>
  <div class="hero-photo" role="img" aria-label="Black and white photo of three people silhouetted against tall windows overlooking a city skyline"></div>
  <div class="hero-panel"></div>
  <div class="hero-line hero-its">It’s</div>
  <div class="hero-line hero-time">TIME To</div>
  <div class="hero-line hero-big">THINK BIG</div>

  <div class="feature" style="left:40px;top:534px">
    <svg width="76" height="74" viewBox="0 0 76 74"><circle cx="38" cy="37" r="22"/><path d="M10 30a29 29 0 0 1 50-14M66 44a29 29 0 0 1-50 14M56 10l4 6-7 2M20 64l-4-6 7-2"/><path d="M44 29c-2-3-12-3-12 2s12 3 12 9-10 5-13 1M38 24v26"/></svg>
    Purchase or Refinance<br>up to 3 Million</div>
  <div class="feature" style="left:218px;top:534px">
    <svg width="56" height="74" viewBox="0 0 56 74"><path d="M4 4h48v66H4z"/><path d="M14 50h28M14 58h28M34 40h8"/><path d="M34 16c-2-3-11-3-11 1s11 3 11 8-9 5-12 1M28 12v24"/></svg>
    No Income Docs or<br>Bank Statements</div>
  <div class="feature" style="left:397px;top:534px">
    <svg width="78" height="74" viewBox="0 0 78 74"><path d="M4 70h70M8 70V30L32 4l24 26v40M56 40h18v30M20 38h20v10H20zM24 56h14v14H24zM60 48h10M8 30h48"/></svg>
    Vacant Properties<br>Allowed</div>
  <div class="feature" style="left:586px;top:534px">
    <svg width="80" height="74" viewBox="0 0 80 74"><path d="M6 44 44 6l30 30-38 38z"/><path d="M14 36 52 -2M20 42l34-34" transform="translate(0,6)"/><path d="M52 30l8-8 6 6-8 8zM18 56l8-8"/></svg>
    Minimum Credit<br>Score 620</div>

  <div class="feature" style="left:114px;top:707px">
    <svg width="80" height="74" viewBox="0 0 80 74"><path d="M4 20h56v34H4z"/><circle cx="32" cy="37" r="9"/><path d="M10 14l44-8 4 14"/><ellipse cx="66" cy="44" rx="10" ry="4"/><path d="M56 44v22c0 5 20 5 20 0V44M56 52c0 5 20 5 20 0M56 60c0 5 20 5 20 0"/></svg>
    Cash Out up to 80%</div>
  <div class="feature" style="left:322px;top:707px">
    <svg width="80" height="74" viewBox="0 0 80 74"><path d="M4 4h64v60H4zM4 14h64M14 34l8 8 16-16"/><path d="M50 60l16-26 6 4-16 26-8 4z"/></svg>
    Same Day Pre-Approval</div>
  <div class="feature" style="left:529px;top:707px">
    <svg width="80" height="74" viewBox="0 0 80 74"><path d="M4 8h60v56H4zM4 20h60M16 2v12M32 2v12M48 2v12M18 46l8 8 16-16"/><circle cx="64" cy="58" r="12"/><path d="M64 52v6h5"/></svg>
    20-30 Day Close</div>

  <div class="brand-card"><span class="mark"></span><span class="brand-name">Bluecrest Lending Group, Inc.</span></div>
  <div class="contact-band"></div>
  <div class="agent-photo" role="img" aria-label="Portrait photo of loan officer Marcus Whitfield in a dark suit"></div>
  <p class="call-line">Call <strong>Marcus Whitfield</strong> today...</p>
  <ul class="contact-list">
    <li>Phone: (800) 641-2957 x 17</li>
    <li>Direct: (240) 958-2074</li>
    <li>www.bluecrestlendhub.com</li>
    <li>NMLS #583617 / #47081</li>
  </ul>
  <div class="social" aria-label="Social links"><span></span><span></span><span></span></div>
  <div class="footer-rule"></div>
</main>
</body>
</html>
```